computter lessons

new business venture [ self employed ] will register my business name as " KEYVORLAN "
what I will offer is :-
computer lessons for new beginners.
Initial set up and basic overview.
lessons per hour in the comfort of your own home.
special rates for customers aged 50+
First lesson is half price with no obligation for booking any further appointments.
a learning and training plan will be presented based on your requirements.
an appraisal update on your new skills.

contact info:-
0161 4970213
07700 900482
larkden@mervoxmail.com

```html
<!DOCTYPE html>
<html lang="en">
<head>
<meta charset="utf-8">
<title>Keyvorlan – Computer Lessons</title>
<link rel="stylesheet" href="https://fonts.googleapis.com/css2?family=Bebas+Neue&family=Raleway:wght@300;400&display=swap">
<style>
  :root {
    --bg: #000000;
    --red: #e3161d;
    --red-fold: #9e0d12;
    --blue: #2b7cc4;
    --white: #ffffff;
    --heading-grey: #d4d4d4;
    --art-tone: #2e2e2e;
    --art-tone-soft: #151515;
  }
  * { margin: 0; padding: 0; box-sizing: border-box; }
  html, body { width: 1200px; height: 850px; overflow: hidden; background: var(--bg); }
  .flyer {
    position: relative;
    width: 1200px;
    height: 850px;
    background: var(--bg);
    font-family: "Bebas Neue", "Oswald", sans-serif;
    color: var(--white);
    overflow: hidden;
  }

  .circuit-art {
    position: absolute;
    left: 520px;
    top: 150px;
    width: 640px;
    height: 670px;
    border-radius: 40px;
    background: radial-gradient(ellipse at 60% 75%, var(--art-tone) 0%, var(--art-tone-soft) 55%, var(--bg) 100%);
  }

  .brand {
    position: absolute;
    left: 78px;
    top: 96px;
    display: flex;
    align-items: center;
    gap: 18px;
  }
  .brand-mark { width: 56px; height: 56px; background: var(--blue); }
  .brand-name { font-size: 88px; line-height: 1; letter-spacing: 2px; color: var(--white); }

  .headline {
    position: absolute;
    left: 566px;
    top: 36px;
    font-family: "Raleway", sans-serif;
    font-weight: 300;
    color: var(--heading-grey);
    white-space: nowrap;
    line-height: 1;
  }
  .headline .we { font-size: 76px; letter-spacing: 2px; }
  .headline .offer { font-size: 112px; font-weight: 400; letter-spacing: 1px; }
  .headline .you { font-size: 58px; }

  .ribbon {
    position: absolute;
    display: flex;
    align-items: center;
    white-space: nowrap;
  }
  .ribbon-red {
    left: 0;
    height: 46px;
    padding-left: 34px;
    background: var(--red);
    font-size: 29px;
    letter-spacing: 0.5px;
    clip-path: polygon(0 0, 100% 0, calc(100% - 16px) 50%, 100% 100%, 0 100%);
  }
  .ribbon-offer {
    left: 686px;
    width: 514px;
    height: 106px;
    padding-left: 26px;
    background: var(--red);
    font-size: 29px;
    line-height: 44px;
    letter-spacing: 0.5px;
    white-space: normal;
    clip-path: polygon(14px 0, 100% 0, 100% 100%, 0 100%, 0 14px);
  }
  .ribbon-offer::before {
    content: "";
    position: absolute;
    left: 0; top: 0;
    width: 14px; height: 14px;
    background: var(--red-fold);
    clip-path: polygon(100% 0, 100% 100%, 0 100%);
  }
  .ribbon-contact {
    left: 0;
    height: 50px;
    justify-content: center;
    background: var(--blue);
    font-size: 36px;
    letter-spacing: 1px;
    clip-path: polygon(0 0, 100% 0, calc(100% - 18px) 50%, 100% 100%, 0 100%);
  }
  .ribbon-contact.email { font-size: 22px; }
</style>
</head>
<body>
<main class="flyer">
  <div class="circuit-art" role="img" aria-label="Illustration of white circuit-board traces branching down to a grey microchip"></div>

  <div class="brand">
    <span class="brand-mark"></span>
    <span class="brand-name">KEYVORLAN</span>
  </div>

  <h1 class="headline"><span class="we">WE</span><span class="offer">OFFER</span><span class="you">YOU</span></h1>

  <p class="ribbon ribbon-red" style="top:298px;width:520px;">Computer lessons for new beginners</p>
  <p class="ribbon ribbon-red" style="top:393px;width:598px;">Special rates for customers aged 50+</p>
  <p class="ribbon ribbon-red" style="top:477px;width:566px;">Initial set up and basic overview.</p>
  <p class="ribbon ribbon-red" style="top:567px;width:586px;">An appraisal update on your new skills.</p>

  <p class="ribbon ribbon-offer" style="top:199px;">Lessons per hour in the comfort of<br>your own home.</p>
  <p class="ribbon ribbon-offer" style="top:358px;">First lesson is half price with no obligation<br>for booking any further appointments.</p>
  <p class="ribbon ribbon-offer" style="top:507px;">A learning and training plan will be<br>presented based on your requirements.</p>

  <p class="ribbon ribbon-contact" style="top:657px;width:418px;">07700 900482</p>
  <p class="ribbon ribbon-contact" style="top:716px;width:418px;">0161 4970213</p>
  <p class="ribbon ribbon-contact email" style="top:781px;width:402px;">LARKDEN@MERVOXMAIL.COM</p>
</main>
</body>
</html>
```